Monthly Parking offer

Brief details: -
About the company: Harbourlane Parking is a Car Parking company with car parks all over the world.

Flyer details: Looking to create an A5 flyer to promote monthly parking to new customers

What flyer should READ:

Park for free!

"monthly parking from $10 a day"
park for free until 30th of June 2014
Contact (03) 8472 519
www.harbourlaneparking.com.au

Industry/Entity Type

Parking

Colors
fbee3f
34a6d7
f04a50

```html
<!DOCTYPE html>
<html lang="en">
<head>
<meta charset="utf-8">
<title>Harbourlane Parking – Park for Free</title>
<link href="https://fonts.googleapis.com/css2?family=Josefin+Sans:wght@600;700&family=Roboto+Condensed:wght@400;700&display=swap" rel="stylesheet">
<style>
  :root {
    --sky-deep: #2c5688;
    --sky-mid: #5f86b4;
    --sky-light: #a9c0d8;
    --ground: #b9b6ae;
    --ribbon-red: #d9352f;
    --ribbon-dark: #a8241f;
    --band-red: #e21f26;
    --band-grey: #3b3b3d;
    --footer-yellow: #f9b535;
    --brand-blue: #1f9ad6;
    --navy: #14233f;
    --ink: #1b1b1b;
    --contact-dark: #3a1616;
    --white: #ffffff;
    --url-yellow: #fbee3f;
  }
  * { margin: 0; padding: 0; box-sizing: border-box; }
  html, body { width: 845px; height: 1200px; overflow: hidden; background: var(--white); }
  .flyer {
    position: relative; width: 845px; height: 1200px; overflow: hidden;
    font-family: "Roboto Condensed", Arial, sans-serif;
  }
  .hero-photo {
    position: absolute; left: 0; top: 0; width: 845px; height: 1018px;
    background: linear-gradient(180deg, var(--sky-deep) 0%, var(--sky-mid) 35%, var(--sky-light) 62%, #d4d7da 70%, var(--ground) 86%, #9d998f 100%);
  }
  .headline {
    position: absolute; left: 0; width: 845px; text-align: center;
    font-family: "Josefin Sans", Arial, sans-serif; font-weight: 700;
    font-size: 128px; line-height: 144px; letter-spacing: 10px;
    color: var(--white); top: 78px;
    text-shadow: 3px 4px 0 rgba(20, 35, 63, 0.45), 0 0 2px rgba(0,0,0,0.3);
  }
  .ribbon { position: absolute; left: 54px; top: 518px; width: 732px; height: 120px; }
  .ribbon-text {
    position: absolute; left: 132px; top: 536px; width: 558px; text-align: center;
    font-family: "Josefin Sans", Arial, sans-serif; font-weight: 700;
    font-size: 20px; line-height: 30px; letter-spacing: 2.4px;
    color: var(--white); text-transform: uppercase; white-space: nowrap;
  }
  .contact-band { position: absolute; left: 0; top: 1018px; width: 845px; height: 60px; display: flex; }
  .rewards {
    width: 234px; flex: none; background: var(--band-grey); color: var(--white);
    display: flex; align-items: center; justify-content: center; gap: 12px;
    font-size: 15px; line-height: 18px; letter-spacing: 5px; text-transform: uppercase;
  }
  .rewards-mark { width: 28px; height: 28px; background: var(--band-red); }
  .contact-main {
    flex: 1; min-width: 0; background: var(--band-red);
    display: flex; align-items: center; justify-content: space-between; gap: 16px;
    padding: 0 36px 0 22px; font-weight: 700; white-space: nowrap;
  }
  .web { color: var(--url-yellow); font-size: 21px; }
  .phone { font-size: 22px; color: var(--white); }
  .phone-label { color: var(--contact-dark); margin-right: 6px; }
  .footer {
    position: absolute; left: 0; top: 1078px; width: 845px; height: 122px;
    background: var(--footer-yellow); color: var(--ink);
  }
  .booking { position: absolute; left: 36px; top: 14px; }
  .booking-label { font-size: 10px; font-weight: 700; text-transform: uppercase; }
  .booking-name { display: flex; align-items: center; gap: 6px; margin-top: 4px; font-size: 22px; font-weight: 700; color: var(--brand-blue); line-height: 1; }
  .booking-name i { width: 24px; height: 24px; border-radius: 50%; background: var(--brand-blue); display: inline-block; }
  .conditions { position: absolute; left: 36px; top: 88px; font-size: 11px; }
  .plan { position: absolute; left: 340px; top: 16px; font-size: 16px; font-weight: 700; }
  .follow { position: absolute; left: 362px; top: 50px; display: flex; align-items: center; gap: 6px; font-size: 12px; font-weight: 700; }
  .follow i { width: 22px; height: 22px; background: var(--brand-blue); display: inline-block; }
  .brand { position: absolute; right: 36px; top: 12px; text-align: center; }
  .brand-lockup { display: flex; align-items: center; gap: 6px; }
  .brand-name { font-size: 19px; font-weight: 700; color: var(--navy); line-height: 1.05; text-align: right; }
  .brand-square { width: 54px; height: 54px; background: var(--brand-blue); }
  .tagline { margin-top: 6px; font-size: 13px; font-weight: 700; color: var(--navy); }
</style>
</head>
<body>
<main class="flyer">
  <div class="hero-photo" role="img" aria-label="Orange classic muscle car parked on gravel in front of a grey warehouse under a blue cloudy sky"></div>

  <h1 class="headline">PARK<br>FOR<br>FREE!</h1>

  <svg class="ribbon" viewBox="0 0 732 120" aria-hidden="true">
    <polygon points="0,36 110,36 110,118 0,118 36,77" fill="var(--ribbon-red)"/>
    <polygon points="732,36 622,36 622,118 732,118 696,77" fill="var(--ribbon-red)"/>
    <polygon points="78,92 110,118 110,92" fill="var(--ribbon-dark)"/>
    <polygon points="654,92 622,118 622,92" fill="var(--ribbon-dark)"/>
    <rect x="78" y="0" width="576" height="92" fill="var(--ribbon-red)"/>
    <line x1="86" y1="8" x2="646" y2="8" stroke="#fff" stroke-width="2" stroke-dasharray="7 5"/>
    <line x1="86" y1="84" x2="646" y2="84" stroke="#fff" stroke-width="2" stroke-dasharray="7 5"/>
    <polyline points="0,44 24,44" stroke="#fff" stroke-width="2" stroke-dasharray="7 5" fill="none"/>
    <polyline points="0,110 24,110" stroke="#fff" stroke-width="2" stroke-dasharray="7 5" fill="none"/>
    <polyline points="708,44 732,44" stroke="#fff" stroke-width="2" stroke-dasharray="7 5" fill="none"/>
    <polyline points="708,110 732,110" stroke="#fff" stroke-width="2" stroke-dasharray="7 5" fill="none"/>
  </svg>
  <p class="ribbon-text">Monthly parking from $10 a day plus<br>park for free until 30th of June 2014</p>

  <section class="contact-band">
    <div class="rewards"><span>Skypoint<br>Rewards</span><i class="rewards-mark"></i></div>
    <div class="contact-main">
      <span class="web">www.harbourlaneparking.com.au</span>
      <span class="phone"><span class="phone-label">CONTACT US</span>(03) 8472 519</span>
    </div>
  </section>

  <footer class="footer">
    <div class="booking">
      <div class="booking-label">Book online &amp; save</div>
      <div class="booking-name">reserve a bay <i></i></div>
    </div>
    <p class="conditions">*Conditions apply. Visit harbourlaneparking.com.au/spr</p>
    <p class="plan">Plan before you Park</p>
    <div class="follow">Follow us <i></i><i></i></div>
    <div class="brand">
      <div class="brand-lockup">
        <span class="brand-name">Harbourlane<br>Parking</span>
        <span class="brand-square"></span>
      </div>
      <p class="tagline">No Parking Worries</p>
    </div>
  </footer>
</main>
</body>
</html>
```